Album Artwork Design: Colorado Reggae-Funk-Hip-Hop Band

We're looking for someone to design the album artwork for our new record. The Denver, CO based reggae/rock/hip-hop/jam band is called "B-Roz and the Current". We're looking for front and back panels.

The album is called "Edge of the Lantern", talking about the seasons of life and how its all part of the ride. We were imagining two hands slightly cupped together with a light orb coming out of the palms (or one singular hand). The light has roots that go into the hands and project interesting/psychedelic objects/patterns outward. Potentially a black background.

We're open to other ideas, that was just one the band as a collective thought was cool. Would like it to be colorful and eye-catching but still clean and professional looking.

The Current depicts the band; uplifting, energetic, positive, ect.

Attached below are recordings of the songs, cool album covers we like and some rough logo ideas (please feel free to disregard if you have a better idea). Much thanks for all submissions!

Target Market(s)

Hippies, nature lovers, party people, positive people, music lovers, ect.

Industry/Entity Type

Entertainment

Logo Text

B-Roz and the Current

Requirements
Must have
• Logo for "B-Roz and the Current" - Band name
• Also on the front need "Edge of the Lantern" - Album Name
• Back side needs tracks listings and room for credits:
• 1. Toward Shores We Won't Reach
• 2. Wildflower Over Rivers
• 3. Moon Slides Down
• 4. Alleys of Tamberlin
• 5. We Could Be Free
• 6. Out In Your Glow
• 7. Raise One For Kindness
• Produced & Engineered by Dorian Pellwick & Vellbrook Audio
• © Ruben Ostrander-Hale 2017
• www.brozandthecurrent.example
Nice to have
• Elements of nature (sun, moon, trees, mountains, ect.)
• Psychedelic/visually captivating elements.
• Clean & professional color scheme/branding.
• Should be authentic and have a distinct style.
Should not have
• Anything cheesy & tacky.

```html
<!DOCTYPE html>
<html lang="en">
<head>
<meta charset="UTF-8">
<title>B-Roz and the Current — Edge of the Lantern</title>
<link rel="stylesheet" href="https://fonts.googleapis.com/css2?family=Open+Sans:wght@400;600;800&display=swap">
<style>
  :root {
    --backdrop: #ececec;
    --paper: #f7f8fa;
    --ink-light: #ffffff;
    --night: #0b0a0d;
    --swirl-blue: #2f6fe0;
    --swirl-teal: #3fc6c9;
    --swirl-green: #8fd87a;
    --swirl-purple: #8a55d6;
    --swirl-pink: #e27fb5;
    --glow-red: #e8472e;
    --glow-orange: #f39a2b;
    --glow-yellow: #e8d23a;
    --hub-ring: #1d2a3a;
  }
  * { margin: 0; padding: 0; box-sizing: border-box; }
  html, body { width: 1200px; height: 662px; overflow: hidden; }
  body {
    background: var(--backdrop);
    font-family: "Open Sans", Arial, sans-serif;
    position: relative;
  }
  .spread {
    position: absolute;
    left: 50px;
    top: 141px;
    width: 760px;
    height: 380px;
    display: flex;
  }
  .panel { position: relative; width: 380px; height: 380px; overflow: hidden; }
  .front-art {
    position: absolute; inset: 0;
    background:
      radial-gradient(circle at 48% 45%, var(--swirl-blue) 0%, rgba(47,111,224,0.75) 16%, rgba(63,198,201,0.55) 32%, rgba(255,255,255,0) 55%),
      radial-gradient(circle at 78% 30%, rgba(143,216,122,0.8) 0%, rgba(143,216,122,0) 38%),
      radial-gradient(circle at 22% 18%, rgba(63,198,201,0.55) 0%, rgba(63,198,201,0) 35%),
      radial-gradient(circle at 55% 85%, rgba(138,85,214,0.75) 0%, rgba(138,85,214,0) 40%),
      radial-gradient(circle at 88% 80%, rgba(226,127,181,0.55) 0%, rgba(226,127,181,0) 35%),
      var(--paper);
  }
  .band-name {
    position: absolute;
    left: 0; right: 0; top: 118px;
    text-align: center;
    color: var(--ink-light);
    font-weight: 800;
    font-size: 27px;
    line-height: 36px;
    letter-spacing: 0.5px;
    text-transform: uppercase;
    text-shadow: 0 1px 2px rgba(20,40,90,0.35);
  }
  .album-title {
    position: absolute;
    left: 0; right: 0; top: 270px;
    text-align: center;
    color: var(--ink-light);
    font-weight: 800;
    font-size: 22px;
    letter-spacing: 0.3px;
    text-transform: uppercase;
    text-shadow: 0 1px 2px rgba(60,40,110,0.35);
  }
  .back-art {
    position: absolute; inset: 0;
    background:
      radial-gradient(circle at 50% 42%, var(--glow-orange) 0%, var(--glow-red) 18%, rgba(232,210,58,0.6) 30%, rgba(138,85,214,0.55) 48%, rgba(11,10,13,0) 66%),
      radial-gradient(circle at 85% 50%, rgba(138,85,214,0.6) 0%, rgba(138,85,214,0) 35%),
      radial-gradient(circle at 40% 75%, rgba(143,216,122,0.45) 0%, rgba(143,216,122,0) 30%),
      var(--night);
  }
  .track-list {
    position: absolute;
    left: 0; right: 0; top: 158px;
    list-style: none;
    text-align: center;
    color: var(--ink-light);
    font-size: 8.5px;
    line-height: 11.5px;
    font-weight: 600;
  }
  .credits {
    position: absolute;
    left: 0; right: 0; bottom: 0;
    text-align: center;
    color: var(--ink-light);
    font-size: 8px;
    line-height: 11px;
    opacity: 0.9;
  }
  .disc {
    position: absolute;
    left: 850px;
    top: 156px;
    width: 330px;
    height: 330px;
  }
  .disc-title { font-family: "Open Sans", Arial, sans-serif; font-weight: 800; font-size: 19px; fill: var(--ink-light); }
  .disc-tracks { font-family: "Open Sans", Arial, sans-serif; font-size: 8px; font-weight: 600; fill: var(--ink-light); }
</style>
</head>
<body>
  <section class="spread">
    <article class="panel front-cover">
      <div class="front-art" role="img" aria-label="Psychedelic swirl of fine colourful light strands in blue, teal, green and purple on white"></div>
      <h1 class="band-name">B-Roz<br>and the<br>Current</h1>
      <h2 class="album-title">Edge of the Lantern</h2>
    </article>
    <article class="panel back-cover">
      <div class="back-art" role="img" aria-label="Glowing swirl of light strands in red, orange, yellow and purple on black"></div>
      <ol class="track-list">
        <li>- 1. Toward Shores We Won't Reach</li>
        <li>- 2. Wildflower Over Rivers</li>
        <li>- 3. Moon Slides Down</li>
        <li>- 4. Alleys of Tamberlin</li>
        <li>- 5. We Could Be Free</li>
        <li>- 6. Out In Your Glow</li>
        <li>- 7. Raise One For Kindness</li>
      </ol>
      <p class="credits">Produced &amp; Engineered by Dorian Pellwick &amp; Vellbrook Audio<br>© Ruben Ostrander-Hale 2017<br>www.brozandthecurrent.example</p>
    </article>
  </section>

  <svg class="disc" viewBox="0 0 330 330" aria-label="Disc label">
    <defs>
      <radialGradient id="disc-swirl" cx="45%" cy="45%" r="60%">
        <stop offset="0" stop-color="#2f6fe0"/>
        <stop offset="0.35" stop-color="#3fc6c9" stop-opacity="0.85"/>
        <stop offset="0.6" stop-color="#8a55d6" stop-opacity="0.7"/>
        <stop offset="1" stop-color="#f7f8fa"/>
      </radialGradient>
      <radialGradient id="disc-green" cx="75%" cy="25%" r="40%">
        <stop offset="0" stop-color="#8fd87a" stop-opacity="0.8"/>
        <stop offset="1" stop-color="#8fd87a" stop-opacity="0"/>
      </radialGradient>
    </defs>
    <g role="img" aria-label="Colourful light-strand swirl printed on the disc">
      <circle cx="165" cy="165" r="160" fill="url(#disc-swirl)"/>
      <circle cx="165" cy="165" r="160" fill="url(#disc-green)"/>
    </g>
    <circle cx="165" cy="165" r="160" fill="none" stroke="#d8dbe0" stroke-width="3"/>
    <circle cx="165" cy="165" r="52" fill="#f5f6f7" stroke="var(--hub-ring)" stroke-width="3"/>
    <circle cx="165" cy="165" r="18" fill="var(--backdrop)" stroke="#c9ccd1" stroke-width="2"/>
    <text class="disc-title" x="165" y="80" text-anchor="middle">EDGE OF THE LANTERN</text>
    <text class="disc-tracks" x="165" y="240" text-anchor="middle">- 1. Toward Shores We Won't Reach</text>
    <text class="disc-tracks" x="165" y="250" text-anchor="middle">- 2. Wildflower Over Rivers</text>
    <text class="disc-tracks" x="165" y="260" text-anchor="middle">- 3. Moon Slides Down</text>
    <text class="disc-tracks" x="165" y="270" text-anchor="middle">- 4. Alleys of Tamberlin</text>
    <text class="disc-tracks" x="165" y="280" text-anchor="middle">- 5. We Could Be Free</text>
    <text class="disc-tracks" x="165" y="290" text-anchor="middle">- 6. Out In Your Glow</text>
    <text class="disc-tracks" x="165" y="300" text-anchor="middle">- 7. Raise One For Kindness</text>
  </svg>
</body>
</html>
```